Cafe menu design

Hi there,

We need a editable menu layout and design to match our new cafe call: " Harlow Bean Roasters", we love the ideas of A4 clip board and self print out menu in black and white. ( Example as attached)

We would like the menu can be break down into category easy for customer to flip around and read. ( example as attached)

Category including the following:

- All day breakfast and Sandwich and Toast
- Main (Lunch&Dinner) and Pizza
- Dessert snacks and nibbles
- Hot and Cold Drinks
- Catering menu

Please find our logo and our current menu as attached for your information and convenience.
Updates

Dear Designers, Thank you for your time and submission, Please find our drink menu and logo as attached. Kind Regards,

Target Market(s)

Young family, young Couple, office and corporate staff

Industry/Entity Type

Cafe

Font styles to use
Serif
Sans Serif

```html
<!DOCTYPE html>
<html lang="en">
<head>
<meta charset="utf-8">
<title>Harlow Bean Roasters – Menu</title>
<link rel="stylesheet" href="https://fonts.googleapis.com/css2?family=Open+Sans:wght@400;600;700;800&family=Oswald:wght@500;600&display=swap">
<style>
:root{
  --stage:#e4e4e4;
  --paper:#ffffff;
  --ink:#1b1b1b;
  --muted:#8a8a8a;
  --rule:#d6d6d6;
}
*{box-sizing:border-box;margin:0;padding:0}
html,body{width:1200px;height:900px;overflow:hidden}
body{background:radial-gradient(ellipse at 50% 40%,#f0f0f0,var(--stage));display:flex;align-items:center;justify-content:center;font-family:"Open Sans",Arial,sans-serif;color:var(--ink)}
.menu{width:622px;height:876px;background:var(--paper);box-shadow:0 6px 24px rgba(0,0,0,.12);padding:22px 26px;display:grid;grid-template-columns:1fr 1fr;column-gap:28px}
.column{display:flex;flex-direction:column}
.brand{display:flex;align-items:center;justify-content:center;gap:8px;margin:4px 0 10px}
.brand-dot{width:30px;height:30px;border-radius:50%;background:var(--ink)}
.brand-name{font-family:"Open Sans",Arial,sans-serif;font-weight:800;font-size:15px;letter-spacing:.5px;text-transform:uppercase}
.rule{height:1px;background:var(--rule);margin:6px 0}
.section-head{display:flex;justify-content:center;margin:10px 0 8px}
.ribbon{background:var(--ink);color:#fff;font-family:"Oswald",Arial,sans-serif;font-weight:600;font-size:10px;letter-spacing:1.2px;text-transform:uppercase;padding:3px 22px;clip-path:polygon(0 0,100% 0,92% 50%,100% 100%,0 100%,8% 50%)}
.group{font-weight:800;font-size:8px;text-transform:uppercase;margin:6px 0 2px;display:flex;align-items:center;gap:4px}
.group::before{content:"";width:5px;height:5px;border-radius:50%;background:var(--ink)}
.item{display:flex;justify-content:space-between;align-items:baseline;gap:8px;font-weight:700;font-size:8.4px;line-height:1.25;margin-top:5px}
.item .price{font-weight:700;white-space:nowrap}
.item .note{font-weight:400;color:var(--muted)}
.desc{font-size:6.8px;color:var(--muted);line-height:1.3;padding-right:26px}
.footnote{font-size:7px;font-weight:700;color:var(--muted);text-align:center;margin-top:auto;padding-top:8px}
.closing{font-size:7.2px;font-weight:700;color:#555;text-align:center;margin-top:14px;line-height:1.35}
</style>
</head>
<body>
<main class="menu">
  <section class="column">
    <div class="brand"><span class="brand-dot"></span><span class="brand-name">Harlow Bean Roasters</span></div>
    <div class="section-head"><span class="ribbon">All Day Breakfast</span></div>
    <div class="item"><span>Sourdough toast with butter/ jam/peanut butter/Yeast Spread</span><span class="price">1 for 3, 2 for 5</span></div>
    <p class="desc">White or multigrain, extra spreads on request</p>
    <div class="item"><span>Toasted fruit loaf with butter</span><span class="price">5</span></div>
    <p class="desc">Thick cut, served warm</p>
    <div class="item"><span>Pancake with maple syrup, vanilla ice cream &amp; fresh cut banana</span><span class="price">15</span></div>
    <div class="item"><span>Poppy seed / blueberry bagel with cream cheese</span><span class="price">9</span></div>
    <div class="item"><span>Low fat Greek yogurt with banana, toasted muesli, honey &amp; cinnamon</span><span class="price">8</span></div>
    <div class="item"><span>Smoked ham &amp; tasty cheese croissant</span><span class="price">6.5</span></div>
    <div class="item"><span>Tasty cheese &amp; tomato croissant</span><span class="price">6.5</span></div>
    <div class="item"><span>Date Scone with jam &amp; fresh cream</span><span class="price">4.5</span></div>
    <div class="item"><span>Wholemeal sourdough sandwiches:</span><span class="price">8.5</span></div>
    <p class="desc">Ham, cheese &amp; tomato · Chicken, avocado &amp; rocket · Salami, brie &amp; pickles · Egg salad &amp; lettuce</p>
    <div class="item"><span>Hash brown, grilled haloumi, green olive, sourdough &amp; lemon wedge</span><span class="price">15</span></div>
    <div class="item"><span>With Tasmania smoked salmon OR breakfast sausage</span><span class="price"></span></div>

    <div class="section-head"><span class="ribbon">Breakfast with Eggs</span></div>
    <div class="item"><span>2 poached or scrambled eggs with wholemeal sourdough</span><span class="price">10</span></div>
    <p class="desc">Add bacon 4 · Smoked salmon 5 · Sausage 4 · Hash brown 3</p>
    <div class="item"><span>Bacon &amp; eggs panini</span><span class="price">8.5</span></div>
    <p class="desc">Bacon, fried egg, tasty cheese &amp; relish</p>
    <div class="item"><span>Double bacon, egg &amp; hash brown roll</span><span class="price">10</span></div>
    <p class="desc">Served on a toasted brioche bun</p>
    <div class="item"><span>Tropical omelette with toasted sourdough</span><span class="price">13</span></div>
    <p class="desc">Ham, pineapple, capsicum, onion &amp; cheese</p>
    <div class="item"><span>Eggs benedict</span><span class="price">13</span></div>
    <p class="desc">Poached eggs, spinach, ham or salmon with hollandaise</p>
    <div class="item"><span>Harlow well-being brekky</span><span class="price">18</span></div>
    <p class="desc">Poached eggs, avocado, grilled tomato, mushroom &amp; spinach on sourdough</p>
    <div class="item"><span>Harlow mighty brekky</span><span class="price">18</span></div>
    <p class="desc">Eggs, bacon, sausage, hash brown, mushroom, tomato &amp; toast</p>
    <p class="footnote">We use sourdough, panini and brioche buns from The Loaf &amp; Crumb Bakery</p>
  </section>

  <section class="column">
    <div class="section-head"><span class="ribbon">Main</span></div>
    <div class="group">Meat</div>
    <div class="item"><span>Gourmet Panini</span><span class="price">10</span></div>
    <p class="desc">Chicken, ham or salami with salad</p>
    <div class="item"><span>Aussie barbeque beef ribs</span><span class="price">16</span></div>
    <div class="item"><span>Steak Aussie beef burger</span><span class="price">14</span></div>
    <div class="item"><span>Chicken schnitzel parmesan burger</span><span class="price">16</span></div>
    <div class="group">Seafood</div>
    <div class="item"><span>Grilled Tasmania salmon fillet</span><span class="price">18</span></div>
    <div class="item"><span>Classic fish &amp; chips</span><span class="price">18</span></div>
    <div class="item"><span>Barramundi fish burger</span><span class="price">15</span></div>
    <div class="group">Vegetarian</div>
    <div class="item"><span>Grilled haloumi &amp; green olives</span><span class="price">15</span></div>
    <div class="item"><span>Vegetarian burger</span><span class="price">15</span></div>
    <div class="group">Kids</div>
    <div class="item"><span>Kids Fish &amp; Chips</span><span class="price">10</span></div>
    <div class="item"><span>Kids Chicken &amp; Chips</span><span class="price">10</span></div>
    <div class="item"><span>Wholemeal sourdough with Cocoa-Nut chocolate spread</span><span class="price">7.5</span></div>

    <div class="section-head"><span class="ribbon">Tapas</span></div>
    <div class="item"><span>Bucket of chips with Aioli</span><span class="price">7.5</span></div>
    <div class="item"><span>Potato wedges with sour cream &amp; sweet chilli jam</span><span class="price">7.5</span></div>
    <div class="item"><span>Grilled haloumi with green olives</span><span class="price">9</span></div>
    <div class="item"><span>Grilled sausage</span><span class="price">7</span></div>
    <div class="item"><span>Mini beef burger <span class="note">(sliders) 3 pieces</span></span><span class="price">9</span></div>
    <div class="item"><span>Italian board to share</span><span class="price">22</span></div>
    <p class="desc">Salami, prosciutto, olives, cheese &amp; sourdough</p>
    <div class="item"><span>Bucket of spicy devil chicken wings <span class="note">5 pieces</span></span><span class="price">10</span></div>
    <div class="item"><span>Crispy salt &amp; pepper calamari</span><span class="price">10</span></div>
    <div class="item"><span>Meatballs flame grilled with aioli &amp; cranberry jam</span><span class="price">12</span></div>

    <div class="section-head"><span class="ribbon">Sweets</span></div>
    <div class="item"><span>Bread &amp; butter pudding <span class="note">(Served warm with fresh cream)</span></span><span class="price">12</span></div>
    <div class="item"><span>Melting Belgian Chocolate Pudding <span class="note">(Served warm with ice cream)</span></span><span class="price">12</span></div>
    <div class="item"><span>American brownie <span class="note">(With fresh cream)</span></span><span class="price">7</span></div>
    <div class="item"><span>Honey pancake <span class="note">(With golden syrup, banana &amp; vanilla ice cream)</span></span><span class="price">7</span></div>
    <div class="item"><span>Belgian chocolate Waffles One/Two</span><span class="price">6 / 10</span></div>
    <p class="desc">(Crunchy waffle with chocolate sauce)</p>
    <div class="item"><span>Belgian chocolate Waffles &amp; Ice Cream One/Two</span><span class="price">8.5 / 15</span></div>
    <p class="desc">(Waffles, fresh banana, vanilla ice cream, chocolate sauce)</p>
    <p class="closing">For more selection of cheesecakes, tarts &amp; desserts,<br>please check out our cake display cabinet</p>
  </section>
</main>
</body>
</html>
```